依頼詳細
商品や価格帯を口頭でしか伝えられてないので、チラシでこんな感じのものでどのくらいの価格帯かを伝えるチラシを作っていただきたいです。
記載項目
●社名:Whistling Meadow(ホイッスリング メドウ)
●電話番号:072-555-0148
●mail:whistling.meadow@mailqorvex.com
●URL:http://w-meadow-qorvex.com/
●料金プラン:
お祝い・記念日・誕生日など様々なシーンに!
バルーンアレンジメント・・\5,000~

結婚式・開店祝いなどメッセージカードをつけて!
バルーンブーケ・・・・・・\5,000~

フラワースタンドを圧倒するインパクト!
バルーンスタンド・・・・・\25,000~

各種イベントの演出に!
バルーンアーチ・・・・・・\40,000~

季節のデコレーションからプロポーズ演出まで!
バルーンデコレーション・・\50,000~

●キャッチコピー:To create a dream and smile
●ロゴ:添付ファイル
●商品写真:添付ファイル
●発送:大阪北摂エリア無料配達いたします。【バルーンギフト・ブーケは全国発送可能※一部離島を除く】
●ご予算・ご希望に応じてオリジナルでお作り致します。
作り置きはしておりません。在庫に限りがございますので、お早目のご予約をおすすめいたします。
どんなことでもお気軽にご相談下さい。
サイズ
A4
ページ数
片面
希望イメージ
シンプル 複雑
単色 カラフル
暗い 明るい
日常 高級
遊び心 厳粛
未来的 伝統的
女性的 男性的
希望する色
ロゴデザインがポップで、カラーがオレンジですが、あまり安っぽくない感じの色目でお願いします。
納品ファイル
• 高解像度JPG (.jpg)
• イラストレーター形式 (.ai)
• フォトショップ形式 (.psd)
• PNG形式 (.png)
補足説明
参考にサンプルチラシを添付します。
添付データ漏れていたのでアップします。
画象1点追加しました。(バルーンアレンジメント02)
■ 選んだ理由

たくさんの提案の中、本当に悩みに悩んで決めさせていただきました。
社員ともども色使いが落ち着いている中で上品に仕上げてくれている点を気に入り今回選ばせていただきました。

■ 提案者全員のお礼・コメント

このたびはたくさんのご提案をありがとうございました。
本当に素晴らしい作品ばかりで、悩みに悩み、決めるのに時間がかかり申し訳ございませんでした。
また、今後も色々とハコニワークを利用していきますので、またの機会によろしくお願いいたします。
本当にありがとうございました。

```html
<!DOCTYPE html>
<html lang="ja">
<head>
<meta charset="utf-8">
<title>Whistling Meadow バルーンチラシ</title>
<link rel="stylesheet" href="https://fonts.googleapis.com/css2?family=M+PLUS+Rounded+1c:wght@500;800&family=Noto+Sans+JP:wght@400;700&display=swap">
<style>
:root{
  --sun:#f6b41e;
  --sun-deep:#f09a14;
  --orange:#ee7d1a;
  --orange-dark:#d8620c;
  --shadow:#c9740c;
  --white:#ffffff;
  --ink:#5a3208;
  --red:#d8363a;
  --pink:#e98ab6;
  --purple:#9b6fbf;
  --green:#4ea86a;
  --teal:#58b8b0;
}
*{margin:0;padding:0;box-sizing:border-box}
html,body{width:876px;height:1200px;overflow:hidden;background:var(--white)}
.flyer{position:relative;width:876px;height:1200px;overflow:hidden;font-family:"Noto Sans JP",sans-serif;color:var(--ink)}
.field{position:absolute;left:0;top:0;width:876px;height:915px;background:radial-gradient(circle at 50% 40%,#fbc63a 0%,var(--sun) 55%,var(--sun-deep) 100%)}
.catch{position:absolute;font-family:"M PLUS Rounded 1c",sans-serif;font-weight:800;color:var(--white);line-height:1;letter-spacing:-2px;white-space:nowrap;
  text-shadow:3px 3px 0 var(--shadow),6px 6px 0 var(--shadow),9px 9px 0 var(--shadow),12px 12px 0 rgba(201,116,12,.6)}
.catch--to{left:210px;top:36px;font-size:140px}
.catch--create{left:190px;top:186px;font-size:140px}
.catch--dream{left:20px;top:490px;font-size:140px}
.catch--and{left:615px;top:500px;font-size:110px}
.catch--smile{left:260px;top:662px;font-size:140px}
.photo{position:absolute;border-radius:18px}
.photo--bouquet{left:40px;top:40px;width:120px;height:360px;border-radius:60px;background:linear-gradient(180deg,var(--red),#b52530 60%,#7a4a2a)}
.photo--arrange{left:590px;top:70px;width:260px;height:140px;border-radius:70px;background:linear-gradient(120deg,var(--pink),var(--purple) 60%,#f4f0f6)}
.photo--arch{left:560px;top:300px;width:290px;height:310px;border-radius:145px 145px 10px 10px;background:transparent;border:38px solid;border-bottom:none;border-color:var(--purple) #e85a8a var(--red) #5b7fd0}
.photo--deco{left:60px;top:770px;width:150px;height:130px;border-radius:65px;background:linear-gradient(160deg,var(--teal),var(--green))}
.photo--stand{left:330px;top:620px;width:120px;height:280px;border-radius:60px;background:linear-gradient(180deg,var(--pink),#c95e8e 55%,#6f8a3e)}
.photo--plant{left:730px;top:800px;width:100px;height:105px;border-radius:50px 50px 10px 10px;background:linear-gradient(180deg,#6aa84f,#3f7a33)}
.label{position:absolute;font-size:12px;line-height:1.45;color:var(--ink)}
.label b{display:block;font-size:14px;color:var(--white);background:var(--orange);padding:1px 6px;margin-top:2px;border-radius:3px;width:max-content}
.label--bouquet{left:40px;top:410px;width:280px}
.label--arrange{left:590px;top:14px;width:260px}
.label--arch{left:690px;top:622px;width:170px}
.label--stand{left:470px;top:822px;width:220px}
.label--deco{left:30px;top:706px;width:260px}
.note{position:absolute;left:40px;top:650px;width:250px;font-size:11px;line-height:1.5;color:var(--ink)}
.intro{position:absolute;left:330px;top:350px;width:430px;padding:10px 14px;background:rgba(216,98,12,.88);color:var(--white);font-size:16px;font-weight:700;line-height:1.6}
.contact{position:absolute;left:0;top:915px;width:876px;height:125px;background:var(--white)}
.phone{position:absolute;left:40px;top:10px;display:flex;align-items:center;gap:10px;font-family:"M PLUS Rounded 1c",sans-serif;font-weight:800;font-size:56px;color:var(--orange-dark);letter-spacing:1px}
.web{position:absolute;left:44px;top:82px;font-size:13px;line-height:1.5;color:var(--ink)}
.delivery{position:absolute;left:560px;top:26px;width:290px;font-size:12px;line-height:1.6;color:var(--ink)}
.footer{position:absolute;left:0;top:1040px;width:876px;height:160px;background:var(--orange);display:flex;align-items:center;justify-content:center;gap:14px}
.brand-dot{width:44px;height:44px;border-radius:50%;background:var(--white)}
.brand{font-family:"M PLUS Rounded 1c",sans-serif;font-weight:800;font-size:40px;color:var(--white)}
</style>
</head>
<body>
<main class="flyer">
  <section class="field">
    <div class="photo photo--bouquet" role="img" aria-label="メッセージカード付きの赤いバルーンブーケの写真"></div>
    <div class="photo photo--arrange" role="img" aria-label="ピンクと紫のバルーンアレンジメントの写真"></div>
    <div class="photo photo--arch" role="img" aria-label="カラフルなバルーンアーチの写真"></div>
    <div class="photo photo--deco" role="img" aria-label="緑のバルーンデコレーションの写真"></div>
    <div class="photo photo--stand" role="img" aria-label="花を添えたバルーンスタンドの写真"></div>
    <div class="photo photo--plant" role="img" aria-label="観葉植物とバルーンの装飾の写真"></div>

    <div class="catch catch--to">To</div>
    <div class="catch catch--create">create</div>
    <div class="catch catch--dream">a dream</div>
    <div class="catch catch--and">and</div>
    <div class="catch catch--smile">smile</div>

    <p class="intro">バルーン専門店「ホイッスリング メドウ」です。<br>ご予算に応じてオリジナルでお作りいたします。<br>どんなことでもお気軽にお電話下さい。</p>

    <p class="label label--arrange">お祝い・記念日・誕生日など様々なシーンに!<b>バルーンアレンジメント ¥5,000~</b></p>
    <p class="label label--bouquet">結婚式・開店祝いなどメッセージカードをつけて!<b>バルーンブーケ ¥5,000~</b></p>
    <p class="label label--arch">各種イベントの演出に!<b>バルーンアーチ ¥40,000~</b></p>
    <p class="note">作り置きはしておりません。在庫に限りがございますので、お早目のご予約をおすすめいたします。</p>
    <p class="label label--deco">季節のデコレーションからプロポーズ演出まで!<b>バルーンデコレーション ¥50,000~</b></p>
    <p class="label label--stand">フラワースタンドを圧倒するインパクト!<b>バルーンスタンド ¥25,000~</b></p>
  </section>

  <section class="contact">
    <div class="phone">
      <svg width="44" height="44" viewBox="0 0 24 24" aria-hidden="true"><path fill="#d8620c" d="M6.6 10.8a15.1 15.1 0 0 0 6.6 6.6l2.2-2.2c.3-.3.7-.4 1-.2 1.1.4 2.3.6 3.6.6.6 0 1 .4 1 1V20c0 .6-.4 1-1 1A17 17 0 0 1 3 4c0-.6.4-1 1-1h3.5c.6 0 1 .4 1 1 0 1.3.2 2.5.6 3.6.1.3 0 .7-.2 1z"/></svg>
      072-555-0148
    </div>
    <p class="web">mail：whistling.meadow@mailqorvex.com<br>URL：http://w-meadow-qorvex.com/</p>
    <p class="delivery">大阪北摂エリア無料配達いたします。<br>【バルーンギフト・ブーケは全国発送可能<br>※一部離島を除く】</p>
  </section>

  <footer class="footer">
    <span class="brand-dot"></span>
    <span class="brand">Whistling Meadow</span>
  </footer>
</main>
</body>
</html>
```